Ledger Ready Business Card

I need a business card designed around my logo (which was designed here on Sketch Yard!)

Target Market(s)

Professional Businesses

Industry/Entity Type

Business

Requirements
Must have
• Details that must be on the business card:

Harriet Vantos
Director
0491 263 358
harriet@ledgerready.com.au
www.ledgerready.com.au
PO Box 4471 Harlow Park Vic 3990

```html
<!DOCTYPE html>
<html lang="en">
<head>
<meta charset="utf-8">
<title>Ledger Ready – Business Card</title>
<link rel="stylesheet" href="https://fonts.googleapis.com/css2?family=Cormorant+Garamond:wght@500;600&display=swap">
<style>
  :root {
    --page-bg: #e9e6e1;
    --card-white: #ffffff;
    --card-grey: #e4e4e4;
    --brand-red: #c8101e;
    --brand-red-light: #e3202c;
    --brand-red-dark: #8e0a12;
    --ink: #1d1d1d;
    --rule: #b9b9b9;
  }
  * { margin: 0; padding: 0; box-sizing: border-box; }
  html, body {
    width: 1200px; height: 1024px; overflow: hidden;
    background: var(--page-bg);
  }
  .canvas {
    width: 1200px; height: 1024px;
    display: flex; flex-direction: column; align-items: center; justify-content: center;
    gap: 52px;
  }
  .card {
    position: relative;
    width: 760px; height: 434px;
    border-radius: 4px;
    overflow: hidden;
    box-shadow: 0 6px 18px rgba(0,0,0,.18);
    font-family: "Cormorant Garamond", serif;
  }

  /* Front */
  .card-front {
    background: linear-gradient(135deg, var(--card-white) 0%, var(--card-white) 45%, var(--card-grey) 100%);
  }
  .front-band {
    position: absolute; left: 0; right: 0; bottom: 0; height: 44px;
    background: linear-gradient(90deg, var(--brand-red-dark), var(--brand-red) 50%, var(--brand-red-light));
  }
  .brand {
    position: absolute; left: 48px; top: 104px;
    display: flex; align-items: center; gap: 16px;
  }
  .brand-square { width: 34px; height: 34px; background: var(--brand-red); }
  .brand-name {
    font-weight: 600; font-size: 38px; color: var(--ink); line-height: 1;
  }
  .person {
    position: absolute; right: 56px; top: 100px; text-align: left;
  }
  .person-name {
    font-weight: 600; font-size: 26px; color: var(--brand-red); line-height: 1.1;
  }
  .person-title {
    font-weight: 600; font-size: 17px; color: var(--ink); letter-spacing: 1px; margin-top: 6px;
    text-transform: uppercase;
  }
  .divider {
    position: absolute; left: 0; right: 0; top: 200px;
    height: 1px; background: var(--rule);
  }
  .contacts {
    position: absolute; left: 56px; top: 228px;
    list-style: none;
  }
  .contacts li {
    display: flex; align-items: center; gap: 16px;
    font-weight: 500; font-size: 21px; color: var(--ink); height: 34px;
  }
  .contacts svg { width: 18px; height: 18px; fill: var(--brand-red); flex: none; }

  /* Back */
  .card-back {
    background: radial-gradient(ellipse at 62% 48%, var(--brand-red-light) 0%, var(--brand-red) 45%, var(--brand-red-dark) 100%);
  }
  .back-brand {
    position: absolute; left: 52px; top: 64px;
    display: flex; align-items: center; gap: 14px;
  }
  .back-brand .brand-square { background: var(--card-white); width: 30px; height: 30px; }
  .back-brand .brand-name { color: var(--card-white); font-size: 34px; }
</style>
</head>
<body>
<main class="canvas">

  <section class="card card-front" aria-label="Business card front">
    <div class="brand">
      <div class="brand-square"></div>
      <div class="brand-name">Ledger Ready</div>
    </div>

    <div class="person">
      <div class="person-name">Harriet Vantos</div>
      <div class="person-title">Director</div>
    </div>

    <div class="divider"></div>

    <ul class="contacts">
      <li>
        <svg viewBox="0 0 24 24" aria-hidden="true"><path d="M6.6 10.8a15.1 15.1 0 0 0 6.6 6.6l2.2-2.2a1 1 0 0 1 1-.25 11.4 11.4 0 0 0 3.6.57 1 1 0 0 1 1 1V20a1 1 0 0 1-1 1A17 17 0 0 1 3 4a1 1 0 0 1 1-1h3.5a1 1 0 0 1 1 1c0 1.25.2 2.45.57 3.6a1 1 0 0 1-.25 1z"/></svg>
        0491 263 358
      </li>
      <li>
        <svg viewBox="0 0 24 24" aria-hidden="true"><path d="M3 5h18a1 1 0 0 1 1 1v12a1 1 0 0 1-1 1H3a1 1 0 0 1-1-1V6a1 1 0 0 1 1-1zm9 7.2L20 7H4z"/></svg>
        harriet@ledgerready.com.au
      </li>
      <li>
        <svg viewBox="0 0 24 24" aria-hidden="true"><path d="M12 2a10 10 0 1 0 0 20 10 10 0 0 0 0-20zm6.9 6h-3a15.6 15.6 0 0 0-1.4-3.6A8 8 0 0 1 18.9 8zM12 4a14 14 0 0 1 1.9 4h-3.8A14 14 0 0 1 12 4zM4.3 14a8 8 0 0 1 0-4h3.4a16.5 16.5 0 0 0 0 4zm.8 2h3a15.6 15.6 0 0 0 1.4 3.6A8 8 0 0 1 5.1 16zm3-8h-3a8 8 0 0 1 4.4-3.6A15.6 15.6 0 0 0 8.1 8zM12 20a14 14 0 0 1-1.9-4h3.8A14 14 0 0 1 12 20zm2.3-6H9.7a14.7 14.7 0 0 1 0-4h4.6a14.7 14.7 0 0 1 0 4zm.2 5.6a15.6 15.6 0 0 0 1.4-3.6h3a8 8 0 0 1-4.4 3.6zm1.8-5.6a16.5 16.5 0 0 0 0-4h3.4a8 8 0 0 1 0 4z"/></svg>
        www.ledgerready.com.au
      </li>
      <li>
        <svg viewBox="0 0 24 24" aria-hidden="true"><path d="M12 2a7 7 0 0 0-7 7c0 5.2 7 13 7 13s7-7.8 7-13a7 7 0 0 0-7-7zm0 9.5A2.5 2.5 0 1 1 12 6.5a2.5 2.5 0 0 1 0 5z"/></svg>
        PO Box 4471 Harlow Park Vic 3990
      </li>
    </ul>

    <div class="front-band"></div>
  </section>

  <section class="card card-back" aria-label="Business card back">
    <div class="back-brand">
      <div class="brand-square"></div>
      <div class="brand-name">Ledger Ready</div>
    </div>
  </section>

</main>
</body>
</html>
```